Bluestone Advisory & Mgmt - Professional Business Cards

Hi!

I am a Real Estate Developer and Construction Consultant.

I have a lot of inspiration from previous designs and would be open to using the attached Designs as a starting point. I would like to see these styles incorporated into your designs.

I really need professional business card to go with it that includes my important info.

Look forward to seeing your designs!.

Target Market(s)

My Target market are building owners, lawyers, consultants.

Industry/Entity Type

Real Estate Development

Contact Information for Business Card

My Name: Dorian Pelkey
My Title: Principle
Company Name: Bluestone Advisory & Mgmt, LLC
Address: 348 West 71st Street, 9th FL New York, NY 10010
Mobile: 917.806.3971
Website: bam-hvx.example

Font styles to use
Serif
Sans Serif

Colors

Designer to choose colors to be used in the design.

Requirements
Must have
• Must incorporate the logo attached or have new that looks similar.
• Must use professional font that will be seen and judged by wealthy land owners and developers.
• Must incorporate some of the color green.
Should not have
• Photo's or pictures of people or buildings of any kind.

```html
<!DOCTYPE html>
<html lang="en">
<head>
<meta charset="utf-8">
<title>Bluestone Advisory &amp; Mgmt – Business Cards</title>
<link rel="stylesheet" href="https://fonts.googleapis.com/css2?family=Raleway:wght@400&family=Mulish:wght@700&family=Questrial&family=Lato:ital@1&display=swap">
<style>
  :root {
    --bg: #ececec;
    --card: #ffffff;
    --green: #78b57c;
    --rule: #7fae82;
    --ink: #444444;
    --ink-dark: #2e2e2e;
    --white: #ffffff;
  }
  * { margin: 0; padding: 0; box-sizing: border-box; }
  html, body { width: 1200px; height: 800px; overflow: hidden; }
  body { background: var(--bg); position: relative; }

  .card {
    position: absolute;
    left: 316px;
    width: 570px;
    height: 330px;
  }
  .card--front { top: 52px; background: var(--card); }
  .card--back { top: 412px; background: var(--green); }

  .brand-name {
    font-family: "Raleway", sans-serif;
    font-weight: 400;
    line-height: 1.1;
  }
  .card--front .brand-name {
    position: absolute;
    right: 23px;
    top: 34px;
    width: 170px;
    text-align: right;
    font-size: 24px;
    color: var(--green);
  }
  .card--back .brand-name {
    position: absolute;
    left: 0; right: 0;
    top: 112px;
    text-align: center;
    font-size: 40px;
    color: var(--white);
  }

  .person {
    position: absolute;
    left: 27px;
    top: 186px;
  }
  .person__name {
    font-family: "Mulish", sans-serif;
    font-weight: 700;
    font-size: 19px;
    color: var(--green);
  }
  .person__title {
    margin-top: 3px;
    font-family: "Lato", sans-serif;
    font-style: italic;
    font-size: 14px;
    color: var(--ink-dark);
  }
  .divider {
    position: absolute;
    left: 91px;
    right: 23px;
    top: 221px;
    height: 1px;
    background: var(--rule);
  }

  .contact-list {
    position: absolute;
    left: 27px;
    top: 245px;
    list-style: none;
    font-family: "Questrial", sans-serif;
    font-size: 14px;
    color: var(--ink);
  }
  .contact-list li {
    display: flex;
    align-items: center;
    height: 21px;
  }
  .contact-list svg {
    width: 9px; height: 9px;
    margin-right: 6px;
    fill: var(--green);
  }

  .address {
    position: absolute;
    right: 23px;
    top: 270px;
    text-align: right;
    font-family: "Questrial", sans-serif;
    font-size: 14px;
    line-height: 17px;
    color: var(--ink);
    font-style: normal;
  }
</style>
</head>
<body>
  <section class="card card--front" aria-label="Business card front">
    <div class="brand-name">Bluestone Advisory &amp; Mgmt</div>

    <div class="person">
      <div class="person__name">Dorian Pelkey</div>
      <div class="person__title">Principle</div>
    </div>
    <div class="divider"></div>

    <ul class="contact-list">
      <li>
        <svg viewBox="0 0 10 10" aria-hidden="true"><path d="M2.2 0.8l1.6 1.8-0.9 1.2c0.6 1.3 1.6 2.3 2.9 2.9l1.2-0.9 1.8 1.6-1 1.6C4.5 9 1 5.5 0.9 1.8z"/></svg>
        917.806.3971
      </li>
      <li>
        <svg viewBox="0 0 10 10" aria-hidden="true"><path d="M0.5 2h9v6.5h-9z M1.2 2.6l3.8 3 3.8-3" stroke="#fff" stroke-width="0.8"/></svg>
        dorian@bam-hvx.example
      </li>
      <li>
        <svg viewBox="0 0 10 10" aria-hidden="true"><circle cx="5" cy="5" r="4.5"/><path d="M0.5 5h9M5 0.5c-2 2.5-2 6.5 0 9M5 0.5c2 2.5 2 6.5 0 9" stroke="#fff" stroke-width="0.7" fill="none"/></svg>
        www.bam-hvx.example
      </li>
    </ul>

    <address class="address">
      348 West 71st Street, 9th FL<br>
      New York, NY 10010
    </address>
  </section>

  <section class="card card--back" aria-label="Business card back">
    <div class="brand-name">Bluestone<br>Advisory &amp; Mgmt</div>
  </section>
</body>
</html>
```